Webdesign für Brandt Maler
Zielgruppe
Maler- und Bodenlegerarbeiten, Farbenherstellung, Fachmarkt
ZieIgruppe sind alle, die Fraben und/oder die Dienstleistungen der Firma benötigen
Aufgabenstellung
dem Kunde gefällt die Seite http://www.maler-quirinus.example/
bitte alle Uploads beachten
eigene Bilder und Stockmaterial

```html
<!DOCTYPE html>
<html lang="de">
<head>
<meta charset="utf-8">
<title>Brandt Maler – Ihr Profi mit langjähriger Erfahrung</title>
<link rel="stylesheet" href="https://fonts.googleapis.com/css2?family=Open+Sans:wght@400;600;700&family=Open+Sans+Condensed:wght@700&family=Roboto+Condensed:wght@400&display=swap">
<style>
  :root {
    --page-white: #ffffff;
    --brand-navy: #3d4196;
    --nav-blue: #4b4fa0;
    --hero-dark: #5d6270;
    --hero-mid: #a3a7b0;
    --hero-light: #e6e3d6;
    --accent-red: #d3111a;
    --text-light: #ffffff;
  }
  * { margin: 0; padding: 0; box-sizing: border-box; }
  html, body {
    width: 1200px;
    height: 800px;
    overflow: hidden;
    background: var(--page-white);
  }
  .site {
    width: 1200px;
    height: 800px;
    display: flex;
    flex-direction: column;
  }
  .site-header {
    height: 140px;
    display: flex;
    flex-direction: column;
    align-items: center;
    justify-content: center;
    gap: 22px;
    background: var(--page-white);
    box-shadow: 0 2px 6px rgba(0,0,0,0.12);
    position: relative;
    z-index: 2;
  }
  .brand-name {
    font-family: "Open Sans", sans-serif;
    font-weight: 700;
    font-size: 26px;
    color: var(--brand-navy);
    letter-spacing: 0.2px;
  }
  .main-nav {
    display: flex;
    gap: 24px;
    list-style: none;
  }
  .main-nav a {
    font-family: "Roboto Condensed", sans-serif;
    font-size: 14px;
    color: var(--nav-blue);
    text-decoration: none;
    text-transform: uppercase;
  }
  .hero {
    flex: 1;
    position: relative;
    display: flex;
    flex-direction: column;
    align-items: center;
    justify-content: center;
    padding-top: 120px;
  }
  .hero-image {
    position: absolute;
    inset: 0;
    background: linear-gradient(100deg, var(--hero-dark) 0%, var(--hero-mid) 35%, var(--hero-light) 55%, var(--hero-light) 100%);
  }
  .hero-content {
    position: relative;
    text-align: center;
    color: var(--text-light);
    text-shadow: 2px 3px 4px rgba(0,0,0,0.7);
  }
  .hero-title {
    font-family: "Open Sans Condensed", "Open Sans", sans-serif;
    font-weight: 700;
    font-size: 44px;
    letter-spacing: 0.5px;
    text-transform: uppercase;
  }
  .hero-services {
    font-family: "Open Sans Condensed", "Open Sans", sans-serif;
    font-weight: 700;
    font-size: 30px;
    margin-top: 14px;
  }
  .hero-cta {
    display: inline-block;
    margin-top: 22px;
    padding: 0 34px;
    height: 58px;
    line-height: 58px;
    background: var(--accent-red);
    color: var(--text-light);
    font-family: "Open Sans Condensed", "Open Sans", sans-serif;
    font-weight: 700;
    font-size: 18px;
    text-decoration: none;
    text-shadow: none;
    border-radius: 2px;
  }
</style>
</head>
<body>
<div class="site">
  <header class="site-header">
    <div class="brand-name">Brandt Maler</div>
    <nav>
      <ul class="main-nav">
        <li><a href="#">Home</a></li>
        <li><a href="#">Leistungen</a></li>
        <li><a href="#">Aktuelle Meldungen</a></li>
        <li><a href="#">Über uns</a></li>
        <li><a href="#">Referenzen</a></li>
        <li><a href="#">Kontakt</a></li>
      </ul>
    </nav>
  </header>
  <section class="hero">
    <div class="hero-image" role="img" aria-label="Farbroller mit Firmenaufdruck auf teilweise grau gestrichener Wand"></div>
    <div class="hero-content">
      <h1 class="hero-title">Ihr Profi mit langjähriger Erfahrung</h1>
      <p class="hero-services">Maler - Bodenlegerarbeiten - Farbenherstellung - Fachmarkt</p>
      <a class="hero-cta" href="#">Anfrage stellen</a>
    </div>
  </section>
</div>
</body>
</html>
```